Digital Agency Needs a Relaunch

We are looking for a modern, top-notch design to elevate our brand to win new clients. It has to build on the clarity of message in the current wireframes and must fit together well on Wordpress.

The winning designer will need to complete the other pages, but please focus on the homepage as the base of your proposed designs for us.

Use the existing logo as a point, and the colour scheme should be around that, we currently use these colours, but you can suggest new mixes:
Purple: #5c306b
Orange: #e27927
Grey: #5f4f61
Light grey: #cacaca
Off white: #ececec
Blue: #674ea7
Updates

Target Market(s)

Decent Sized SME Businesses (20+ Staff, Over £1m turnover)

Industry/Entity Type

Digital Marketing

Number of Pages Required

5+ page

Font styles to use
Sans Serif

Colors

Designer to choose colors to be used in the design.

Requirements
Must have
• A real attention on the design piece. Ignore the current website and really focus on the messaging and the brief.
Nice to have
• Read the messages and think about the impact. Use the purple in the logo more than the orange, but try to keep it smart rather than cool
Should not have
• Inconsistent design, serif fonts, stock images and not meeting the wireframes.

```html
<!DOCTYPE html>
<html lang="en">
<head>
<meta charset="utf-8">
<title>Vanta Digital — Growth works for you</title>
<link href="https://fonts.googleapis.com/css2?family=Poppins:wght@400;500;600&display=swap" rel="stylesheet">
<style>
:root{
  --purple:#5c306b;
  --purple-deep:#3b2a5e;
  --violet:#674ea7;
  --orange:#e27927;
  --ink:#1e1a22;
  --grey:#5f4f61;
  --muted:#a8a2ad;
  --light:#ececec;
  --white:#ffffff;
  --footer-link:#b7aad4;
}
*{box-sizing:border-box;margin:0;padding:0}
html,body{width:1200px;height:4668px;overflow:hidden}
body{font-family:"Poppins",sans-serif;color:var(--ink);background:var(--white);position:relative}
.abs{position:absolute}
a{color:inherit;text-decoration:none}

/* header */
.brand{left:44px;top:32px;display:flex;align-items:center;gap:8px;font-size:28px;font-weight:500;color:var(--purple);white-space:nowrap}
.brand-dot{width:14px;height:14px;border-radius:50%;background:var(--orange)}
.util-nav{right:66px;top:29px;display:flex;font-size:11px;white-space:nowrap}
.util-nav span{padding:0 18px;border-left:1px solid #cacaca;line-height:14px}
.util-nav span:first-child{border-left:0}
.util-nav span:last-child{padding-right:0}
.nav-item{top:69px;font-size:13px;font-weight:500;white-space:nowrap}

/* hero */
.hero{left:44px;top:120px;width:1116px;height:585px;border-radius:30px;overflow:hidden;
  background:linear-gradient(160deg,#4a2f7e 0%,#3e2c72 55%,#352863 100%)}
.hero-art{position:absolute;inset:0}
.hero h1{position:absolute;left:0;right:0;top:220px;text-align:center;font-weight:600;font-size:52px;line-height:76px;color:var(--white);text-shadow:0 3px 10px rgba(0,0,0,.35)}
.hero h1 em{font-style:normal;color:#c9aff0}

/* intro */
.section-title{left:0;width:1200px;text-align:center;font-weight:500;font-size:40px;line-height:60px}
.section-title .accent{color:var(--purple)}
.intro-col{width:288px;font-size:16px;line-height:25px}
.intro-col .lead{color:var(--violet)}
.line-icon{width:60px;height:60px}

/* cta bars */
.cta-bar{background:var(--purple);border-radius:16px;display:flex;align-items:center;justify-content:space-between;color:var(--white);font-size:25px;font-weight:500}
.btn{background:var(--orange);color:var(--white);border-radius:6px;font-size:19px;font-weight:500;display:flex;align-items:center;gap:10px;justify-content:center;white-space:nowrap}

/* services */
.panel-grey{background:var(--light);border-radius:30px}
.service{background:var(--white);border-radius:18px;width:254px;height:365px}
.service .ico{position:absolute;left:30px;top:40px}
.service h3{position:absolute;left:30px;top:168px;font-size:23px;font-weight:600}
.service ul{position:absolute;left:30px;top:212px;list-style:none;font-size:14px;line-height:31px;white-space:nowrap}

/* pain/gain */
.pain{left:40px;top:1897px;width:1125px;height:281px;background:var(--violet);border-radius:20px;color:var(--white)}
.badge{left:42px;top:28px;background:var(--purple);border-radius:5px;font-size:12px;letter-spacing:1px;padding:4px 8px;font-weight:500}
.pain-rule{left:0;right:0;top:72px;height:1px;background:rgba(255,255,255,.35)}
.pain h3{font-size:30px;font-weight:600}
.pain p{font-size:19px;line-height:24px}

/* growth */
.growth-glow{left:370px;top:2255px;width:500px;height:300px;
  background:radial-gradient(ellipse 110px 150px at 90px 150px,rgba(126,224,234,.28),transparent 70%),
             radial-gradient(ellipse 110px 120px at 206px 200px,rgba(183,166,207,.28),transparent 70%),
             radial-gradient(ellipse 120px 170px at 304px 120px,rgba(242,185,138,.3),transparent 70%)}
.growth-col{width:305px;font-size:16px;line-height:25px}
.growth-col .lead{color:var(--violet)}
.statement{left:0;width:1200px;text-align:center;color:var(--violet);font-size:26px;line-height:37px;font-weight:500}

/* case studies */
.case{width:252px;height:306px;border-radius:18px;background:var(--white);border:1px solid #dcdcdc;padding:28px 22px}
.case .num{font-size:33px;color:var(--muted);font-weight:400}
.case h4{margin-top:28px;font-size:20px;font-weight:600;line-height:27px}
.case.active{background:var(--purple);color:var(--white);border:0;box-shadow:0 14px 30px rgba(60,30,80,.35);height:308px}
.case.active .num{color:var(--orange)}
.read{font-size:16px;color:var(--orange);font-weight:500;display:flex;gap:8px;align-items:center}

/* blog */
.post{width:252px;height:337px;border-radius:12px;background:var(--white);border:1px solid #e2e2e2;overflow:hidden}
.post .img{height:195px}
.post .date{margin:20px 18px 0;font-size:12px;color:var(--grey)}
.post .title{margin:12px 18px 0;font-size:15px;line-height:20px}
.post.active{box-shadow:0 10px 26px rgba(0,0,0,.12);height:338px}

/* footer */
.footer{left:0;top:4098px;width:1200px;height:570px;background:var(--purple-deep);color:var(--white);overflow:hidden}
.footer-glow{left:620px;top:200px;width:580px;height:370px;
  background:radial-gradient(ellipse 160px 200px at 130px 230px,rgba(63,111,208,.28),transparent 70%),
             radial-gradient(ellipse 180px 240px at 380px 180px,rgba(177,58,122,.26),transparent 70%)}
.footer h5{font-size:18px;font-weight:500}
.footer ul{list-style:none;margin-top:6px;font-size:16px;line-height:31px;color:var(--footer-link);white-space:nowrap}
.footer .contact{font-size:16px;color:var(--footer-link);display:flex;gap:12px;line-height:20px}
.legal{font-size:12px;color:var(--footer-link);white-space:nowrap}
</style>
</head>
<body>

<!-- header -->
<div class="abs brand"><span class="brand-dot"></span>Vanta Digital</div>
<nav class="abs util-nav"><span>Blog</span><span>About Us</span><span>Contact Us</span><span>01632 960 410</span></nav>
<span class="abs nav-item" style="left:600px">Create</span>
<span class="abs nav-item" style="left:702px">Communicate</span>
<span class="abs nav-item" style="left:843px">Convert</span>
<span class="abs nav-item" style="left:951px">Close</span>
<span class="abs nav-item" style="left:1046px">Case Studies</span>

<!-- hero -->
<section class="abs hero">
  <div class="hero-art" role="img" aria-label="Illustration of rising gradient arrows in orange, red, blue and teal"
       style="background:radial-gradient(ellipse 260px 320px at 150px 520px,rgba(200,60,40,.55),transparent 70%),radial-gradient(ellipse 200px 260px at 290px 560px,rgba(20,150,190,.6),transparent 70%),radial-gradient(ellipse 240px 500px at 680px 250px,rgba(220,120,40,.6),transparent 70%),radial-gradient(ellipse 200px 420px at 380px 300px,rgba(20,160,200,.5),transparent 70%),radial-gradient(ellipse 220px 420px at 930px 380px,rgba(30,140,190,.55),transparent 70%)"></div>
  <h1>Growth works for you<br><em>in your targeting</em></h1>
</section>

<!-- intro -->
<h2 class="abs section-title" style="top:760px">Fed Up With Agencies Who Don’t Care?<br><span class="accent">We’ve Heard That Before</span></h2>

<svg class="abs line-icon" style="left:67px;top:978px" viewBox="0 0 60 60" fill="none" stroke="#1e1a22" stroke-width="2"><circle cx="24" cy="17" r="10"/><path d="M6 52c0-12 8-20 18-20s14 5 16 10"/><path d="M40 46l4 4 8-10"/></svg>
<svg class="abs line-icon" style="left:427px;top:978px" viewBox="0 0 60 60" fill="none" stroke="#1e1a22" stroke-width="2"><path d="M28 14c2 10 6 14 16 16-10 2-14 6-16 16-2-10-6-14-16-16 10-2 14-6 16-16z"/><path d="M12 4c1 4 3 6 7 7-4 1-6 3-7 7-1-4-3-6-7-7 4-1 6-3 7-7z"/><path d="M48 42c1 3 2 4 5 5-3 1-4 2-5 5-1-3-2-4-5-5 3-1 4-2 5-5z"/></svg>
<svg class="abs line-icon" style="left:788px;top:978px" viewBox="0 0 60 60" fill="none" stroke="#1e1a22" stroke-width="2"><circle cx="18" cy="22" r="7"/><circle cx="40" cy="14" r="8"/><path d="M36 14l3 3 5-6"/><path d="M6 56c0-10 5-17 12-17s12 7 12 17"/><path d="M30 44c2-8 6-12 12-12s12 7 12 16"/></svg>

<p class="abs intro-col" style="left:67px;top:1052px"><span class="lead">We know every client has unique needs.</span> Yet, few digital agencies spend enough time getting to know the clients Business</p>
<p class="abs intro-col" style="left:427px;top:1052px"><span class="lead">We’re different.</span> We take a highly personalised approach to every project, working closely with our clients to understand their objectives, challenges and target audience</p>
<p class="abs intro-col" style="left:788px;top:1052px;width:322px"><span class="lead">Knowing your business</span> is the first step in helping you grow. It’s how we work, and it will work for you.</p>

<!-- cta 1 -->
<div class="abs cta-bar" style="left:44px;top:1266px;width:1116px;height:99px;padding:0 28px 0 48px">
  <span>Achieve Growth That Works</span>
  <a class="btn" style="width:198px;height:57px"><svg width="18" height="18" viewBox="0 0 24 24" fill="none" stroke="#fff" stroke-width="2"><path d="M5 3h4l2 5-3 2a12 12 0 006 6l2-3 5 2v4a2 2 0 01-2 2A17 17 0 013 5a2 2 0 012-2z"/></svg>Set Up A Call</a>
</div>

<!-- services -->
<section class="abs panel-grey" style="left:40px;top:1427px;width:1125px;height:428px"></section>
<div class="abs service" style="left:67px;top:1453px">
  <svg class="ico" width="44" height="44" viewBox="0 0 44 44"><path d="M8 8l28 28" stroke="#e27927" stroke-width="6" stroke-linecap="round"/><path d="M36 8L8 36" stroke="#3f8fe0" stroke-width="6" stroke-linecap="round"/></svg>
  <h3>Create</h3><ul><li>Branding</li><li>Graphics</li><li>Video</li><li>Content</li></ul>
</div>
<div class="abs service" style="left:338px;top:1453px">
  <svg class="ico" width="44" height="44" viewBox="0 0 44 44"><path d="M6 26l22-14v24z" fill="#c9c4cf"/><circle cx="8" cy="30" r="6" fill="#e24a4a"/><path d="M34 8l4-4M36 16h6M32 4v-3" stroke="#3f8fe0" stroke-width="2.5"/></svg>
  <h3>Communicate</h3><ul><li>Ads</li><li>Social</li><li>Organic</li><li>Email</li></ul>
</div>
<div class="abs service" style="left:608px;top:1453px">
  <svg class="ico" width="44" height="44" viewBox="0 0 44 44" fill="#5aa83a"><circle cx="22" cy="8" r="4"/><circle cx="10" cy="14" r="3.5"/><circle cx="34" cy="14" r="3.5"/><circle cx="22" cy="22" r="4"/><circle cx="10" cy="28" r="3.5"/><circle cx="34" cy="28" r="3.5"/><circle cx="22" cy="36" r="4"/></svg>
  <h3>Convert</h3><ul><li>Websites</li><li>E-Commerce</li><li>Analytics</li><li>Lead Generation</li></ul>
</div>
<div class="abs service" style="left:880px;top:1453px">
  <svg class="ico" width="44" height="44" viewBox="0 0 44 44"><path d="M4 14l12-6 10 6 14-4v12L24 34 4 22z" fill="#f2a93b"/><path d="M14 22l8 6 8-8" stroke="#d07a1a" stroke-width="2.5" fill="none"/></svg>
  <h3 style="top:160px">Close</h3><ul style="top:200px"><li>CRM</li><li>Systems</li><li>Customer Success</li><li>AI &amp; Automations</li></ul>
</div>

<!-- pain / gain -->
<section class="abs pain">
  <span class="abs badge">WEBSITE</span>
  <svg class="abs" style="left:1003px;top:32px" width="70" height="26" viewBox="0 0 70 26"><rect x="9" y="6" width="4" height="14" fill="#fff"/><rect x="17" y="6" width="4" height="14" fill="#fff"/><circle cx="57" cy="13" r="12" fill="#fff"/><path d="M53 7l10 6-10 6z" fill="#674ea7"/></svg>
  <div class="abs pain-rule"></div>
  <h3 class="abs" style="left:42px;top:105px">Your Pain?</h3>
  <p class="abs" style="left:42px;top:165px;width:360px">“I spend most of my development budget fixing errors and bugs”</p>
  <svg class="abs" style="left:415px;top:110px" width="140" height="120" viewBox="0 0 140 120" fill="none" stroke-width="3"><path d="M40 22h60M84 8l16 14-16 14" stroke="#e8906a"/><path d="M20 62h100M104 48l16 14-16 14" stroke="#b48ee6"/><path d="M0 100h70M54 86l16 14-16 14" stroke="#4f9ae0"/></svg>
  <h3 class="abs" style="left:600px;top:105px">Future Gain</h3>
  <p class="abs" style="left:600px;top:158px;width:430px">A fast and reliable cash-generative content managed e-commerce or lead generation website</p>
</section>

<!-- growth -->
<div class="abs growth-glow" role="img" aria-label="Decorative outline illustration of rising arrows in cyan, lilac and peach"></div>
<h2 class="abs section-title" style="top:2436px">Vanta <span class="accent">Where Growth Works</span></h2>

<p class="abs growth-col" style="left:77px;top:2562px"><span class="lead">We understand the importance of a strong online presence.</span> That’s why we offer a complete range of digital marketing solutions to help your reach your growth goals.</p>
<p class="abs growth-col" style="left:438px;top:2562px"><span class="lead">Our track record demostrates expertise in all forms of digital marketing,</span> including Website builds, Searchly Ads, SEO, Email Marketing.</p>
<p class="abs growth-col" style="left:800px;top:2562px;width:330px"><span class="lead">We’re constantly staying up-to-date on the latest trends, tech and best practices in the industry,</span> so you can trust that you’re getting the most effective and efficient stragies for your business growth.</p>

<p class="abs statement" style="top:2792px">Set up a call and we’re confident we can show you where we can add growth and<br>value to your business.</p>

<!-- case studies -->
<section class="abs panel-grey" style="left:40px;top:2930px;width:1125px;height:480px"></section>
<h2 class="abs section-title" style="top:2960px">Create <span class="accent">Case Studies</span></h2>
<article class="abs case" style="left:78px;top:3052px"><div class="num">01</div><h4>Searchly’s New PPC Features are Loaded with AI</h4></article>
<article class="abs case" style="left:342px;top:3052px"><div class="num">02</div><h4>Searchly’s New PPC Features are Loaded with AI</h4></article>
<article class="abs case active" style="left:605px;top:3052px"><div class="num">03</div><h4>Searchly’s New PPC Features are Loaded with AI</h4>
  <a class="read" style="margin-top:48px">Read <svg width="16" height="14" viewBox="0 0 16 14" fill="none" stroke="#e27927" stroke-width="2"><path d="M1 7h13M9 2l5 5-5 5"/></svg></a></article>
<article class="abs case" style="left:870px;top:3052px"><div class="num">04</div><h4>Searchly’s New PPC Features are Loaded with AI</h4></article>

<!-- blog -->
<h2 class="abs section-title" style="top:3470px;color:var(--purple)">From the Blog</h2>
<article class="abs post" style="left:66px;top:3568px">
  <div class="img" role="img" aria-label="Illustration of people celebrating together" style="background:linear-gradient(135deg,#f4f0ea,#dfe8f4 50%,#f7e2d6)"></div>
  <p class="date">12 Dec 2020</p><p class="title">Searchly’s New PPC Features are Loaded with AI</p></article>
<article class="abs post" style="left:330px;top:3568px">
  <div class="img" role="img" aria-label="Illustration of a piggy bank with plants on orange" style="background:#f2552a"></div>
  <p class="date">12 Dec 2020</p><p class="title">How Searchly Killed the Broad Match Keyword?</p></article>
<article class="abs post active" style="left:595px;top:3568px">
  <div class="img" role="img" aria-label="Illustration of a person walking past signposts" style="background:linear-gradient(135deg,#f5b62d,#f2c54a 60%,#e9e3d8)"></div>
  <p class="date">12 Dec 2020</p><p class="title">The 9 Rules of Social Media Engagement (Part II)</p>
  <a class="read" style="margin:22px 18px 0">Read <svg width="16" height="14" viewBox="0 0 16 14" fill="none" stroke="#e27927" stroke-width="2"><path d="M1 7h13M9 2l5 5-5 5"/></svg></a></article>
<article class="abs post" style="left:857px;top:3568px">
  <div class="img" role="img" aria-label="Soft pastel gradient graphic with a large number nine" style="background:linear-gradient(160deg,#e9868c,#f1b58c 50%,#9fd3c0)"></div>
  <p class="date">12 Dec 2020</p><p class="title">The 9 Rules of Social Media Engagement (Part I)</p></article>

<!-- cta 2 -->
<div class="abs cta-bar" style="left:66px;top:3958px;width:1067px;height:99px;padding:0 26px 0 46px;font-size:24px">
  <span>We’re The Turbo Boost For Your Digital Marketing Engine</span>
  <a class="btn" style="width:261px;height:57px">Put Your Foot Down <svg width="18" height="18" viewBox="0 0 24 24" fill="none" stroke="#fff" stroke-width="2"><path d="M22 2L11 13M22 2l-7 20-4-9-9-4z"/></svg></a>
</div>

<!-- footer -->
<footer class="abs footer">
  <div class="abs footer-glow" role="img" aria-label="Decorative outline illustration of rising arrows in blue and magenta"></div>
  <div class="abs" style="left:74px;top:72px"><h5>Create</h5><ul><li>Branding</li><li>Graphics</li><li>Video</li><li>Content</li></ul></div>
  <div class="abs" style="left:299px;top:72px"><h5>Convert</h5><ul><li>Websites</li><li>Lead Generation</li><li>Ecommerce</li><li>Analytics</li></ul></div>
  <div class="abs" style="left:585px;top:72px"><h5>Connect</h5><ul><li>Case Studies</li><li>Blog</li><li>About Us</li></ul></div>
  <div class="abs" style="left:843px;top:72px"><h5>Contact</h5>
    <p class="contact" style="margin-top:14px"><svg width="16" height="16" viewBox="0 0 24 24" fill="none" stroke="#b7aad4" stroke-width="2"><path d="M5 3h4l2 5-3 2a12 12 0 006 6l2-3 5 2v4a2 2 0 01-2 2A17 17 0 013 5a2 2 0 012-2z"/></svg>01632 960 410</p>
    <p class="contact" style="margin-top:28px;width:300px"><svg width="16" height="20" viewBox="0 0 24 28" fill="none" stroke="#b7aad4" stroke-width="2"><path d="M12 26s9-9 9-15a9 9 0 00-18 0c0 6 9 15 9 15z"/><circle cx="12" cy="11" r="3"/></svg>Harbour Point House, Northfield Westshire NF2 4QT</p></div>
  <div class="abs" style="left:74px;top:305px"><h5>Communicate</h5><ul><li>Ads</li><li>Organic</li><li>Social</li><li>Email</li></ul></div>
  <div class="abs" style="left:299px;top:305px"><h5>Close</h5><ul><li>CRM</li><li>Systems</li><li>Customer Success</li><li>AI &amp; Automations</li></ul></div>
  <p class="abs legal" style="left:74px;top:534px">(c) Vanta Digital Limited. All rights reserved</p>
  <p class="abs legal" style="left:748px;top:536px">Sitemap</p>
  <p class="abs legal" style="left:867px;top:536px">Terms of Use</p>
  <p class="abs legal" style="left:1013px;top:536px">Privacy Policy</p>
</footer>

</body>
</html>
```